Web re-vamp for PailMark.com

Website to go along with ArtForge logo winner. Make it look better than the existing Pail1.com or ThePailMark.com current page. Basic. 5 pages. No e-commerce on the product page (no direct sales thru the web site). We have 3 logo's that we can not seem to decide which should be used. Feel free to use any of the the 3 logo's you want (uploaded file) as main logo the rest added somewhere else on the site- if it's too confusing we'll take them off later. Slogan's: CLEAR DAIRY SYSTEMS and Making a Clear Difference. The inventor of this new product LOVES the following page: Vitrelux.com. So any submission should have this feel but try not to copy exactly. Colors: dark blues/dark purples and jewel tones. Professional feel with elegance.
-

Target Market(s)

The farmer is the buyer but sometimes a buying company which buys in bulk for large farms is the target audience. This is not for sale to the general public.

Industry/Entity Type

E-Commerce

Colors
3277b5
876aae
ffffff

Requirements
Must have
• A look with this website in mind (but not identical) www.Vitrelux.com
Colors: rich deep blues, ingido, blue purple jewel tones. PailMarkâ„¢ (Trademark sign) ever time the words appear- together.
Nice to have
• a "click" sound like a cow's mooooo when cursor passes over "contact us"? Just a thought but not a must.
Should not have
• Reds, Pink, Bright blue, Yellow, Orange

```html
<!DOCTYPE html>
<html lang="en">
<head>
<meta charset="utf-8">
<title>Contact Us – PailMark™</title>
<link href="https://fonts.googleapis.com/css2?family=Arimo:wght@400;700&display=swap" rel="stylesheet">
<style>
  :root {
    --bg-deep: #03101d;
    --bg-glow: #0d3458;
    --accent: #1e9be0;
    --accent-line: #3f8fd0;
    --text: #ffffff;
    --text-soft: #d7e3ee;
    --required: #e0323a;
    --field: #ffffff;
    --divider: #12314d;
    --button-top: #f6f9c8;
    --button-bottom: #d4e57a;
    --button-text: #1f2a10;
    --footer-brand: #1d6fa8;
  }
  * { box-sizing: border-box; margin: 0; padding: 0; }
  html, body { width: 1200px; height: 687px; overflow: hidden; }
  body {
    font-family: "Arimo", Arial, sans-serif;
    color: var(--text);
    background:
      radial-gradient(ellipse 420px 300px at 250px 40px, var(--bg-glow) 0%, rgba(13,52,88,0) 100%),
      var(--bg-deep);
    position: relative;
  }
  .brand {
    position: absolute; left: 146px; top: 60px; width: 222px; height: 62px;
    display: flex; flex-direction: column; align-items: center; justify-content: center;
  }
  .brand-name { font-size: 36px; font-weight: 700; color: var(--accent); letter-spacing: 1px; line-height: 1; }
  .brand-tagline { font-size: 9px; letter-spacing: 1.5px; color: var(--text-soft); margin-top: 6px; }
  .search {
    position: absolute; left: 887px; top: 32px; width: 167px; height: 21px;
    background: var(--field); border-radius: 2px; display: flex; justify-content: flex-end;
  }
  .search-button { width: 24px; height: 21px; background: #e6eef5; display: flex; align-items: center; justify-content: center; }
  .main-nav {
    position: absolute; left: 384px; top: 73px; width: 670px; height: 37px;
    border-top: 2px solid var(--accent-line); border-bottom: 3px solid var(--accent-line);
  }
  .main-nav a {
    position: absolute; top: 9px; color: var(--text); text-decoration: none;
    font-size: 12px; line-height: 14px; white-space: nowrap;
  }
  .main-nav a.current { color: var(--accent); }
  .nav-home { left: 17px; }
  .nav-products { left: 78px; }
  .nav-about { left: 167px; }
  .nav-contact { left: 252px; }
  .nav-news { left: 352px; }
  .social { position: absolute; right: 13px; top: 6px; display: flex; gap: 5px; }
  .social span { width: 21px; height: 21px; background: var(--field); border-radius: 2px; display: block; }
  .contact-heading {
    position: absolute; left: 158px; top: 169px; font-size: 22px; font-weight: 700; color: var(--accent);
  }
  .heading-rule { position: absolute; left: 145px; top: 206px; width: 396px; height: 1px; background: var(--divider); }
  .contact-form { position: absolute; left: 158px; top: 224px; width: 370px; }
  .form-note { font-size: 11px; font-weight: 700; color: var(--text-soft); }
  .req { color: var(--required); }
  .field-label { display: block; font-size: 11px; font-weight: 700; color: var(--text-soft); margin-bottom: 4px; }
  .field { background: var(--field); border: none; border-radius: 2px; display: block; }
  .row { display: flex; gap: 10px; margin-top: 14px; }
  .row .col { width: 180px; }
  .row .field { width: 180px; height: 24px; }
  .block { margin-top: 15px; }
  .block .field.email { width: 369px; height: 24px; }
  .block.message { margin-top: 21px; }
  .block .field.message-box { width: 368px; height: 128px; }
  .submit {
    margin-top: 18px; width: 99px; height: 35px; border-radius: 18px; border: none;
    background: linear-gradient(var(--button-top), var(--button-bottom));
    color: var(--button-text); font-family: inherit; font-weight: 700; font-size: 15px;
  }
  .hero-photo {
    position: absolute; left: 586px; top: 172px; width: 456px; height: 393px;
    background: linear-gradient(135deg, #6a5a44 0%, #2a241f 35%, #141312 60%, #8a7350 100%);
  }
  .site-footer { position: absolute; left: 0; top: 607px; width: 1200px; height: 80px; border-top: 1px solid var(--divider); }
  .footer-address {
    position: absolute; left: 146px; top: 12px; font-size: 11px; font-weight: 700;
    font-style: normal; line-height: 15px; color: var(--text);
  }
  .footer-address .phone { color: var(--accent); font-weight: 400; }
  .footer-brand {
    position: absolute; left: 514px; top: 14px; height: 50px; display: flex; align-items: center; gap: 10px;
    font-size: 28px; color: var(--footer-brand);
  }
  .footer-brand .mark { width: 34px; height: 34px; border: 3px solid var(--footer-brand); border-radius: 3px; }
  .footer-legal { position: absolute; left: 834px; top: 27px; font-size: 11px; font-weight: 700; line-height: 16px; }
  .footer-legal .protected { color: var(--accent); font-weight: 400; }
</style>
</head>
<body>
  <header>
    <div class="brand">
      <span class="brand-name">PailMark™</span>
      <span class="brand-tagline">CLEAR DAIRY SYSTEMS</span>
    </div>
    <div class="search">
      <span class="search-button">
        <svg width="13" height="13" viewBox="0 0 13 13"><circle cx="5.5" cy="5.5" r="4" fill="none" stroke="#1e9be0" stroke-width="2"/><line x1="8.5" y1="8.5" x2="12" y2="12" stroke="#1e9be0" stroke-width="2.4"/></svg>
      </span>
    </div>
    <nav class="main-nav">
      <a href="#" class="nav-home">HOME</a>
      <a href="#" class="nav-products">PRODUCTS</a>
      <a href="#" class="nav-about">ABOUT US</a>
      <a href="#" class="nav-contact current">CONTACT US</a>
      <a href="#" class="nav-news">NEWS &amp; ARTICLES</a>
      <div class="social"><span></span><span></span><span></span></div>
    </nav>
  </header>

  <main>
    <h1 class="contact-heading">Contact Us</h1>
    <div class="heading-rule"></div>
    <form class="contact-form">
      <p class="form-note">Your email is never published nor shared. Required fields are marked <span class="req">*</span></p>
      <div class="row">
        <div class="col"><label class="field-label">First Name<span class="req">*</span></label><div class="field"></div></div>
        <div class="col"><label class="field-label">Last Name<span class="req">*</span></label><div class="field"></div></div>
      </div>
      <div class="block"><label class="field-label">E-Mail<span class="req">*</span></label><div class="field email"></div></div>
      <div class="block message"><label class="field-label">Message<span class="req">*</span></label><div class="field message-box"></div></div>
      <button type="button" class="submit">Submit</button>
    </form>
    <div class="hero-photo" role="img" aria-label="Photo of two dairy cows in halters standing at a milking stall rail"></div>
  </main>

  <footer class="site-footer">
    <address class="footer-address">
      Resin Draw Technology (R.D.T.)<br>
      2480 Harlow Road<br>
      Cedar Bay, Florida 33012<br>
      <span class="phone">555-014-2290</span>
    </address>
    <div class="footer-brand"><span class="mark"></span>PailMark™</div>
    <div class="footer-legal">
      PailMark™ and Clear Dairy Systems™<br>
      <span class="protected">Copyright and Trademark protected. 2014</span>
    </div>
  </footer>
</body>
</html>
```